Business Card Design

I'd like to have some business cards designed using my new logo. I am an accountant and company secretary and offer these services through Halvorsen Global Advisory Pty Ltd. I am the sole Director of the company. Please let me know if you require any further logo files.

Industry/Entity Type

Business

```html
<!DOCTYPE html>
<html lang="en">
<head>
<meta charset="utf-8">
<title>Halvorsen Global Advisory – Business Card Options</title>
<link rel="stylesheet" href="https://fonts.googleapis.com/css2?family=Barlow:wght@400;700&family=Crimson+Text:wght@400;600&display=swap">
<style>
  :root {
    --brand-blue: #0075bf;
    --brand-grey: #6d6e71;
    --text-grey: #58595b;
    --paper: #ffffff;
    --frame: #8a8a8a;
    --label: #222222;
  }
  html, body {
    margin: 0;
    padding: 0;
    overflow: hidden;
    background: var(--paper);
  }
  .sheet {
    position: relative;
    width: 1200px;
    height: 796px;
    overflow: hidden;
    background: var(--paper);
    font-family: "Crimson Text", Georgia, serif;
  }
  .option-label {
    position: absolute;
    left: 36px;
    margin: 0;
    font-family: "Barlow", Arial, sans-serif;
    font-weight: 700;
    font-size: 33px;
    color: var(--label);
    letter-spacing: 0.3px;
  }
  .side-label {
    position: absolute;
    width: 406px;
    text-align: center;
    font-family: "Barlow", Arial, sans-serif;
    font-size: 18px;
    color: var(--label);
  }
  .card {
    position: absolute;
    width: 406px;
    height: 262px;
    overflow: hidden;
    box-sizing: border-box;
  }
  .card-front {
    border: 1px solid var(--frame);
    background: var(--paper);
    color: var(--text-grey);
  }
  .card-art {
    position: absolute;
    inset: 0;
  }
  .company-name {
    position: absolute;
    margin: 0;
    font-family: "Crimson Text", Georgia, serif;
    font-weight: 400;
    text-transform: uppercase;
    font-size: 13px;
    line-height: 14px;
    letter-spacing: 0.4px;
  }
  .company-name.on-blue { color: var(--paper); }
  .company-name.on-white { color: var(--brand-grey); }
  .services {
    position: absolute;
    margin: 0;
    padding: 0;
    list-style: none;
    color: var(--paper);
    font-weight: 600;
    font-size: 12.5px;
  }
  .services-centered {
    left: 0;
    right: 0;
    top: 203px;
    text-align: center;
    line-height: 17px;
  }
  .services-stacked {
    left: 40px;
    top: 104px;
    line-height: 16.5px;
  }
  .person-name {
    margin: 0;
    font-size: 19px;
    font-weight: 400;
    line-height: 20px;
  }
  .person-role {
    margin: 0;
    font-size: 11.5px;
    font-weight: 600;
    line-height: 14px;
  }
  .contact {
    margin: 0;
    font-size: 10.5px;
    line-height: 14px;
  }
  .front-block {
    position: absolute;
  }
  .front-block.centered {
    left: 0;
    right: 0;
    text-align: center;
  }
  .front-block.left {
    left: 154px;
  }
</style>
</head>
<body>
<main class="sheet">

  <!-- Option 1 -->
  <h2 class="option-label" style="top:154px;">Option 1</h2>

  <section class="card card-back" style="left:245px; top:37px;" aria-label="Option 1 card back">
    <svg class="card-art" width="406" height="262" viewBox="0 0 406 262" aria-hidden="true">
      <rect width="406" height="262" fill="var(--brand-grey)"/>
      <polygon points="0,0 406,0 406,140 0,176" fill="var(--paper)"/>
      <polygon points="0,0 406,0 406,126 0,160" fill="var(--brand-blue)"/>
    </svg>
    <p class="company-name on-blue" style="left:40px; top:86px;">Halvorsen<br>Global Advisory<br>Pty Ltd</p>
    <ul class="services services-centered">
      <li>Management Accounting &nbsp;•&nbsp; Financial Accounting</li>
      <li>Bookkeeping &nbsp;•&nbsp; Company Secretarial Services</li>
    </ul>
  </section>
  <div class="side-label" style="left:245px; top:316px;">back</div>

  <section class="card card-front" style="left:744px; top:37px;" aria-label="Option 1 card front">
    <p class="company-name on-white" style="left:140px; top:45px;">Halvorsen<br>Global Advisory<br>Pty Ltd</p>
    <div class="front-block centered" style="top:110px;">
      <p class="person-name">Marcus Ellery</p>
      <p class="person-role">Chief Financial Officer</p>
    </div>
    <div class="front-block centered" style="top:155px;">
      <p class="contact">M: 041 555 017 | E: marcus.ellery@hga.com.au</p>
    </div>
    <div class="front-block centered" style="top:195px;">
      <p class="contact">14 Harbourline Terrace Eastvale WA 6999</p>
      <p class="contact">T: 041 555 013 | F: 041 555 018</p>
    </div>
  </section>
  <div class="side-label" style="left:744px; top:316px;">front</div>

  <!-- Option 2 -->
  <h2 class="option-label" style="top:582px;">Option 2</h2>

  <section class="card card-back" style="left:245px; top:465px;" aria-label="Option 2 card back">
    <svg class="card-art" width="406" height="262" viewBox="0 0 406 262" aria-hidden="true">
      <rect width="406" height="262" fill="var(--brand-grey)"/>
      <polygon points="0,0 336,0 286,262 0,262" fill="var(--paper)"/>
      <polygon points="0,0 314,0 264,262 0,262" fill="var(--brand-blue)"/>
    </svg>
    <p class="company-name on-blue" style="left:40px; top:52px;">Halvorsen<br>Global Advisory<br>Pty Ltd</p>
    <ul class="services services-stacked">
      <li>Management Accounting</li>
      <li>Financial Accounting</li>
      <li>Bookkeeping</li>
      <li>Company Secretarial Services</li>
    </ul>
  </section>
  <div class="side-label" style="left:245px; top:748px;">back</div>

  <section class="card card-front" style="left:744px; top:468px;" aria-label="Option 2 card front">
    <p class="company-name on-white" style="left:154px; top:45px;">Halvorsen<br>Global Advisory<br>Pty Ltd</p>
    <div class="front-block left" style="top:116px;">
      <p class="person-name">Marcus Ellery</p>
      <p class="person-role">Chief Financial Officer</p>
    </div>
    <div class="front-block left" style="top:161px;">
      <p class="contact">M: 041 555 017 | E: marcus.ellery@hga.com.au</p>
    </div>
    <div class="front-block left" style="top:196px;">
      <p class="contact">14 Harbourline Terrace Eastvale WA 6999</p>
      <p class="contact">T: 041 555 013 | F: 041 555 018</p>
    </div>
  </section>
  <div class="side-label" style="left:744px; top:748px;">front</div>

</main>
</body>
</html>
```